new marketing company logo and business card

design logo and biz card for marketing start up.

My company name needs a brand logo designed: Cedar Hollow Marketing Co.
Tagline: Sales - Marketing - Brand Building

Sister Bay is the name of my favorite place, in Wisconsin, but the business is NOT BASED there. It should evoke warmth, friendliness, professionalism, and marketing services from a seasoned marketer.

Target Market(s)

I am selling my services to small business that need help.

Industry/Entity Type

Marketing

Contact Information for Business Card

Cedar Hollow Marketing Co. (logo)
Sales - Marketing - Brand Building (tagline)

Maren T. Holloway
MarenTHolloway@quillpost.net
555-014-3926 mobile

Font styles to use
Serif
Sans Serif

Colors
f78f20
f37122
f68d4d
00a990
85cae6
33b8a4
faa54b

Requirements
Must have
• a logo
• a business card
Nice to have
• I'd love to see a small subtle reference to Sister Bay built in. Sister bay is named that because there are two islands called ‘sister islands’ that flank the bay. If you google this you will see.
• I like warm, earthy colors. But, I am a fun, approachable, real person. Not stand-offish. Should be warm and appealing yet professional.
Should not have
• nothing cartoon-ish. no child-like fonts. this is a professional business.

```html
<!DOCTYPE html>
<html lang="en">
<head>
<meta charset="utf-8">
<title>Cedar Hollow Marketing Co. — Business Card</title>
<link rel="stylesheet" href="https://fonts.googleapis.com/css2?family=Montserrat:wght@500;700&family=Oswald:wght@500&family=Open+Sans:wght@400&display=swap">
<style>
  :root {
    --bg: #2b2b2d;
    --card-white: #ffffff;
    --card-shade: #ececec;
    --orange: #f37122;
    --orange-deep: #c8561b;
    --orange-light: #ee6f26;
    --sky: #85cae6;
    --ink: #3d3d3d;
    --ink-soft: #555555;
    --back-type: #d9d9d9;
  }
  * { margin: 0; padding: 0; box-sizing: border-box; }
  html, body { width: 1200px; height: 900px; overflow: hidden; }
  body {
    background: var(--bg);
    display: flex;
    flex-direction: column;
    align-items: center;
    justify-content: center;
    gap: 50px;
    font-family: "Open Sans", sans-serif;
  }
  .card {
    width: 560px;
    height: 320px;
    border-radius: 22px;
    position: relative;
    overflow: hidden;
    box-shadow: 0 10px 28px rgba(0,0,0,.45);
  }
  /* Front */
  .card-front {
    background: linear-gradient(135deg, var(--card-shade) 0%, var(--card-white) 45%, var(--card-white) 100%);
  }
  .brand {
    position: absolute;
    top: 38px;
    right: 40px;
    text-align: left;
  }
  .brand-name {
    font-family: "Montserrat", sans-serif;
    font-weight: 700;
    font-size: 21px;
    letter-spacing: .5px;
    color: var(--orange);
    text-transform: uppercase;
    white-space: nowrap;
  }
  .brand-tagline {
    font-family: "Montserrat", sans-serif;
    font-weight: 500;
    font-size: 12.5px;
    letter-spacing: 3px;
    color: var(--sky);
    margin-top: 6px;
    white-space: nowrap;
  }
  .brand-tagline .mid { color: var(--orange); }
  .person {
    position: absolute;
    top: 132px;
    left: 30px;
    width: 252px;
    text-align: right;
  }
  .person-name {
    font-family: "Oswald", sans-serif;
    font-weight: 500;
    font-size: 29px;
    line-height: 1.05;
    color: var(--orange);
    text-transform: uppercase;
    white-space: nowrap;
  }
  .person-role {
    font-size: 13px;
    color: var(--ink);
    margin-top: 4px;
  }
  .divider {
    position: absolute;
    top: 142px;
    left: 298px;
    width: 1.5px;
    height: 68px;
    background: var(--orange);
  }
  .contact {
    position: absolute;
    top: 142px;
    left: 314px;
    list-style: none;
    font-size: 13px;
    color: var(--ink);
    line-height: 22px;
  }
  .contact li { display: flex; align-items: center; gap: 7px; white-space: nowrap; }
  .contact svg { width: 11px; height: 11px; flex: none; }
  .contact .accent { color: var(--orange); }
  .address {
    position: absolute;
    left: 34px;
    bottom: 38px;
    font-size: 13.5px;
    color: var(--ink-soft);
  }
  /* Back */
  .card-back {
    background: linear-gradient(135deg, var(--orange-deep) 0%, var(--orange-light) 100%);
    display: flex;
    flex-direction: column;
    align-items: center;
    justify-content: center;
  }
  .card-back .brand-name {
    color: var(--back-type);
    font-size: 26px;
  }
  .card-back .brand-tagline {
    color: var(--back-type);
    font-size: 15px;
    letter-spacing: 3.5px;
    margin-top: 8px;
  }
</style>
</head>
<body>
  <section class="card card-front" aria-label="Business card front">
    <div class="brand">
      <div class="brand-name">Cedar Hollow Marketing Co.</div>
      <div class="brand-tagline">Sales - <span class="mid">Marketing</span> - Brand Building</div>
    </div>

    <div class="person">
      <div class="person-name">Maren T. Holloway</div>
      <div class="person-role">Director</div>
    </div>

    <div class="divider"></div>

    <ul class="contact">
      <li>
        <svg viewBox="0 0 12 12" aria-hidden="true"><path d="M3 1.2 4.6 3.4 3.6 4.6c.6 1.4 1.8 2.6 3.2 3.2l1.2-1 2.2 1.6-.9 1.8C5.6 10.2 1.8 6.4 1.2 2.1Z" fill="var(--orange)"/></svg>
        <span>555-014-3926</span>
      </li>
      <li>
        <svg viewBox="0 0 12 12" aria-hidden="true"><rect x="1" y="2.5" width="10" height="7" rx="1" fill="none" stroke="var(--orange)" stroke-width="1.3"/><path d="M1.5 3 6 6.6 10.5 3" fill="none" stroke="var(--orange)" stroke-width="1.2"/></svg>
        <span>MarenTHolloway@quillpost.net</span>
      </li>
      <li>
        <svg viewBox="0 0 12 12" aria-hidden="true"><circle cx="6" cy="6" r="5" fill="none" stroke="var(--orange)" stroke-width="1.2"/><ellipse cx="6" cy="6" rx="2.2" ry="5" fill="none" stroke="var(--orange)" stroke-width="1"/><path d="M1 6h10" stroke="var(--orange)" stroke-width="1"/></svg>
        <span>www.<span class="accent">cedarhollowmktg</span>.com</span>
      </li>
    </ul>

    <div class="address">218 Fernbrook Lane, Millbridge, 40512</div>
  </section>

  <section class="card card-back" aria-label="Business card back">
    <div class="brand-name">Cedar Hollow Marketing Co.</div>
    <div class="brand-tagline">Sales - Marketing - Brand Building</div>
  </section>
</body>
</html>
```